Cole Varga Photography

Would like the Business card to have a cool logo. I’m targeting wedding/ engagement: portrait photography. My phone number on it. And my business email address.

Wedding/portrait/engagement photography.

```html
<!DOCTYPE html>
<html lang="en">
<head>
<meta charset="utf-8">
<title>Cole Varga Photography – Business Card</title>
<link href="https://fonts.googleapis.com/css2?family=Montserrat:wght@400&display=swap" rel="stylesheet">
<style>
  :root {
    --backdrop: #dcd8d3;
    --card: #f1f1ef;
    --ink: #2b2b2b;
    --ink-soft: #4a4a4a;
    --ornament: #b9b9b6;
  }
  html, body {
    margin: 0;
    padding: 0;
    width: 1200px;
    height: 900px;
    overflow: hidden;
    background: var(--backdrop);
    font-family: "Montserrat", sans-serif;
    color: var(--ink);
  }
  .canvas {
    position: relative;
    width: 1200px;
    height: 900px;
  }
  .card {
    position: absolute;
    background: var(--card);
    box-shadow: 0 2px 6px rgba(0,0,0,0.12);
  }
  .card--front {
    left: 208px;
    top: 165px;
    width: 410px;
    height: 255px;
  }
  .card--back {
    left: 560px;
    top: 466px;
    width: 416px;
    height: 260px;
  }
  .front-brand {
    position: absolute;
    left: 0;
    right: 0;
    top: 90px;
    text-align: center;
  }
  .brand-name {
    margin: 0;
    font-size: 27px;
    font-weight: 400;
    letter-spacing: 1px;
    color: var(--ink);
  }
  .services {
    margin: 18px 0 0;
    font-size: 8px;
    letter-spacing: 2.6px;
    color: var(--ink-soft);
    word-spacing: 8px;
  }
  .ornament {
    position: absolute;
    left: 174px;
    width: 66px;
    height: 26px;
    background: var(--ornament);
    border-radius: 13px;
    opacity: 0.55;
  }
  .ornament--top { top: 34px; }
  .ornament--bottom { top: 198px; }
  .back-row {
    position: absolute;
    left: 0;
    right: 0;
    top: 108px;
    display: flex;
    justify-content: center;
    align-items: center;
  }
  .back-brand {
    margin: 0;
    font-size: 14px;
    font-weight: 400;
    letter-spacing: 0.4px;
    color: var(--ink);
    width: 138px;
    text-align: center;
    line-height: 1.3;
  }
  .divider {
    width: 1px;
    height: 38px;
    background: var(--ink-soft);
    margin: 0 14px 0 8px;
  }
  .contact {
    margin: 0;
    font-style: normal;
    font-size: 11px;
    line-height: 1.45;
    color: var(--ink);
  }
</style>
</head>
<body>
  <main class="canvas">
    <section class="card card--front" aria-label="Business card front">
      <div class="front-brand">
        <h1 class="brand-name">Cole Varga Photography</h1>
        <p class="services">WEDDING PORTRAIT LIFESTYLE</p>
      </div>
    </section>

    <section class="card card--back" aria-label="Business card back">
      <div class="ornament ornament--top" role="img" aria-label="Line-drawn leafy sprig ornament"></div>
      <div class="back-row">
        <p class="back-brand">Cole Varga Photography</p>
        <span class="divider"></span>
        <address class="contact">
          555 014 2736<br>
          colevarga@yourmail.com
        </address>
      </div>
      <div class="ornament ornament--bottom" role="img" aria-label="Line-drawn leafy sprig ornament"></div>
    </section>
  </main>
</body>
</html>
```